Flyer für Mobile Massage am Arbeitsplatz
Zielgruppe
Der Flyer richtet sich an Geschäftsleitungen, Firmenvorstände, Betriebsräte.
Ich werde den Flyer sowohl persönlich überreichen, als auch postalisch verschicken.
Aufgabenstellung
Es geht um einen Flyer, DIN lang, Hochformat, beidseitig bedruckt.

```html
<!DOCTYPE html>
<html lang="de">
<head>
<meta charset="utf-8">
<title>Mobile Massage am Arbeitsplatz – Flyer</title>
<link href="https://fonts.googleapis.com/css2?family=Arimo:wght@700&family=Tinos:wght@400;700&family=Gochi+Hand&display=swap" rel="stylesheet">
<style>
  :root {
    --sky: #a7b1dc;
    --sky-light: #c2c9e8;
    --band: #d3d5de;
    --band-edge: #eef0f6;
    --ink: #151515;
    --navy: #0c1030;
    --teal: #2f8f93;
    --white: #ffffff;
    --photo-warm: #b58a55;
    --photo-dark: #6b5335;
  }
  html, body {
    margin: 0;
    padding: 0;
    width: 1200px;
    height: 2494px;
    overflow: hidden;
    background: var(--sky);
  }
  .flyer {
    position: relative;
    width: 1200px;
    height: 2494px;
    overflow: hidden;
    background: linear-gradient(180deg, var(--sky-light) 0%, var(--sky) 40%, var(--sky) 100%);
  }
  .flyer__waves {
    position: absolute;
    inset: 0;
  }
  .flyer__url {
    position: absolute;
    left: 0;
    top: 0;
  }
  .title-card {
    position: absolute;
    left: 296px;
    top: 31px;
    width: 640px;
    height: 312px;
    background: var(--white);
    box-shadow: 10px 12px 18px rgba(40, 40, 70, 0.45);
    display: flex;
    flex-direction: column;
    align-items: center;
    justify-content: center;
    font-family: "Gochi Hand", cursive;
    font-size: 88px;
    line-height: 1.05;
    color: var(--ink);
    text-align: center;
  }
  .intro {
    position: absolute;
    left: 420px;
    width: 780px;
    margin: 0;
    font-family: "Arimo", Arial, sans-serif;
    font-weight: 700;
    font-size: 33px;
    line-height: 50px;
    color: var(--ink);
    text-align: center;
    text-shadow: 0 0 6px rgba(255,255,255,0.9), 0 0 3px rgba(255,255,255,0.9);
  }
  .intro--lead { top: 550px; }
  .intro--benefits { top: 820px; }
  .intro--tax { top: 1350px; }
  .photo {
    position: absolute;
    background: linear-gradient(150deg, #e6d6b8 0%, var(--photo-warm) 55%, var(--photo-dark) 100%);
  }
  .photo--seated { left: 203px; top: 1537px; width: 411px; height: 327px; }
  .photo--shoulders { left: 396px; top: 1923px; width: 439px; height: 315px; }
  .prices {
    position: absolute;
    left: 670px;
    top: 1612px;
    margin: 0;
    font-family: "Tinos", "Times New Roman", serif;
    font-size: 40px;
    line-height: 47px;
    color: var(--ink);
  }
  .phone {
    position: absolute;
    left: 280px;
    top: 2290px;
    margin: 0;
    font-family: "Tinos", "Times New Roman", serif;
    font-size: 64px;
    color: var(--teal);
    letter-spacing: 1px;
  }
</style>
</head>
<body>
<main class="flyer">
  <svg class="flyer__waves" width="1200" height="2494" viewBox="0 0 1200 2494" aria-hidden="true">
    <path d="M0 720 C 300 560, 700 420, 1200 370 L 1200 1420 C 850 1470, 400 1480, 0 1560 Z" fill="var(--band)"/>
    <path d="M0 720 C 300 560, 700 420, 1200 370" fill="none" stroke="var(--band-edge)" stroke-width="14"/>
    <path d="M0 1560 C 400 1480, 850 1470, 1200 1420" fill="none" stroke="var(--band-edge)" stroke-width="10" opacity="0.8"/>
  </svg>

  <svg class="flyer__url" width="200" height="2494" viewBox="0 0 200 2494" aria-label="www.mobile-massage-spree-havelland.de">
    <text transform="translate(140 2325) rotate(-90)" textLength="2140" lengthAdjust="spacingAndGlyphs"
          font-family="Tinos, 'Times New Roman', serif" font-weight="700" font-size="118" fill="var(--navy)">www.mobile-massage-spree-havelland.de</text>
  </svg>

  <div class="title-card">
    <span>Mobile Massage</span>
    <span>am Arbeitsplatz</span>
  </div>

  <p class="intro intro--lead">In unseren Massagen am Arbeitsplatz lassen wir<br>Elemente aus der Shiatsu - Energiemassage und<br>den Joint Release - Gelenklockerungen<br>zusammenfließen.</p>

  <p class="intro intro--benefits">Auf diese Weise eröffnen wir einen Raum für<br>spürbare Entspannung mitten im Arbeitsalltag.<br>Die Massagen befreien aus berufsbedingten<br>Zwangshaltungen, wirken stresslindernd und<br>stimmungshebend im Team ,<br>fokussieren auf die Problemzonen im Büro:<br>Rücken, Nacken, Schulter und Mausarm<br>und sind ein Baustein im innerbetrieblichen<br>Gesundheitsmanagement.</p>

  <p class="intro intro--tax">Die Kosten können, sofern vom Arbeitgeber<br>getragen, nach §3 Nr.34 EstG von der Steuer<br>abgesetzt werden.</p>

  <div class="photo photo--seated" role="img" aria-label="Foto: Masseur behandelt eine Person auf einem Massagestuhl"></div>

  <p class="prices">Preise:<br>20 Minuten : 16 Euro<br>inklusive Anfahrt<br>buchbar ab 4 Personen</p>

  <div class="photo photo--shoulders" role="img" aria-label="Foto: Schultermassage auf dem Massagestuhl"></div>

  <p class="phone">Tel.: 030 - 48219730</p>
</main>
</body>
</html>
```